Construction APP

We need to design a modern app IOS/Android where my team can create a profile with their info, (maybe share some pictures), reviews, submit time cards, show their availability, etc.

Like a taxi app but for construction. We also want to be able to assign each team member to a project manager with who they currently working. So we will also need to be able to create profiles at the Administration level.

The goal is to keep innovating the app as we grow, so we are always open to suggestions and ideas.

Low design quality

Industry/Entity Type

Construction

Colors
FFC000
F8CF3A
FAE287
FDF2CF
FEFAEE

Requirements
Must have
• IOS/Android APP where my team can create a profile with their info, (maybe share some pictures), reviews, submit time cards, show their availability, etc.We also want to be able to assign each team member to a project manager with who they currently working. So we will also need to be able to create profiles at the Administration level.

```html
<!DOCTYPE html>
<html lang="en">
<head>
<meta charset="UTF-8">
<title>Crewline – Sign In</title>
<link rel="stylesheet" href="https://fonts.googleapis.com/css2?family=Oswald:wght@600&family=Source+Sans+3:wght@400;600;700&display=swap">
<style>
  :root {
    --screen-bg: #f3f3f3;
    --field-bg: #ffffff;
    --ink: #1a1a1a;
    --ink-soft: #3c3c3c;
    --gold: #b38128;
    --night: #161616;
    --white: #ffffff;
  }
  * { box-sizing: border-box; margin: 0; padding: 0; }
  html, body { width: 1200px; height: 2394px; overflow: hidden; }
  body {
    background: var(--screen-bg);
    font-family: "Source Sans 3", "Source Sans Pro", sans-serif;
    color: var(--ink);
    position: relative;
  }
  .brand {
    position: absolute; top: 470px; left: 0; width: 1200px;
    display: flex; justify-content: center; align-items: center; gap: 22px;
  }
  .brand-dot { width: 44px; height: 44px; border-radius: 50%; background: var(--gold); }
  .brand-name {
    font-family: "Source Sans 3", "Source Sans Pro", sans-serif;
    font-weight: 700; font-size: 72px; letter-spacing: 4px; color: var(--ink);
  }
  .headline {
    position: absolute; top: 715px; left: 0; width: 1200px; text-align: center;
    font-family: "Oswald", "Fjalla One", sans-serif; font-weight: 600;
    font-size: 118px; line-height: 1; letter-spacing: -1px; color: var(--ink);
  }
  .subhead {
    position: absolute; top: 845px; left: 0; width: 1200px; text-align: center;
    font-size: 56px; color: var(--ink-soft);
  }
  .field-label {
    position: absolute; left: 160px; font-weight: 700; font-size: 48px; color: var(--ink);
  }
  .label-name { top: 1002px; }
  .label-password { top: 1232px; }
  .field {
    position: absolute; left: 164px; width: 872px; height: 124px;
    background: var(--field-bg); border-radius: 14px;
    box-shadow: 0 4px 14px rgba(0,0,0,0.07);
    display: flex; align-items: center; gap: 26px; padding-left: 40px;
    font-size: 50px; color: var(--ink-soft);
  }
  .field-name { top: 1078px; }
  .field-password { top: 1303px; }
  .field-icon { width: 42px; height: 42px; flex: none; }
  .forgot-link {
    position: absolute; top: 1456px; right: 164px;
    font-weight: 600; font-size: 40px; color: var(--ink); letter-spacing: 0.5px;
  }
  .worksite {
    position: absolute; left: 0; top: 1620px; width: 1200px; height: 620px;
    background: linear-gradient(180deg, rgba(190,190,190,0) 0%, #c9c9c9 25%, #9a9a9a 55%, #4a4a4a 80%, var(--night) 100%);
  }
  .sign-in {
    position: absolute; top: 1533px; left: 164px; width: 872px; height: 124px;
    background: var(--gold); border-radius: 12px;
    display: flex; align-items: center; justify-content: center;
    font-weight: 700; font-size: 56px; letter-spacing: 2px; color: var(--white);
  }
  .footer-band {
    position: absolute; left: 0; bottom: 0; width: 1200px; height: 170px;
    background: var(--night);
    display: flex; align-items: center; justify-content: center;
  }
  .create-account { font-weight: 600; font-size: 44px; color: var(--white); letter-spacing: 0.5px; }
</style>
</head>
<body>
  <div class="brand">
    <span class="brand-dot"></span>
    <span class="brand-name">CREWLINE</span>
  </div>

  <h1 class="headline">WELCOME BACK!</h1>
  <p class="subhead">Sign in to your account</p>

  <label class="field-label label-name">Name</label>
  <div class="field field-name">
    <svg class="field-icon" viewBox="0 0 24 24" fill="none" stroke="#1a1a1a" stroke-width="1.6">
      <circle cx="12" cy="8" r="4.2"/>
      <path d="M4 21c0-3.5 3.6-5.5 8-5.5s8 2 8 5.5z" stroke-linejoin="round"/>
    </svg>
    <span>Enter your name</span>
  </div>

  <label class="field-label label-password">Password</label>
  <div class="field field-password">
    <svg class="field-icon" viewBox="0 0 24 24" fill="none" stroke="#1a1a1a" stroke-width="1.6">
      <rect x="4.5" y="10" width="15" height="12" rx="2.5"/>
      <path d="M8 10V7a4 4 0 0 1 8 0v3"/>
      <path d="M12 14.5v3" stroke-linecap="round"/>
    </svg>
    <span>Enter your Password</span>
  </div>

  <span class="forgot-link">Forgot Password?</span>

  <div class="worksite" role="img" aria-label="Silhouette scene of a construction site with cranes, scaffolding, an excavator and workers"></div>

  <div class="sign-in">SIGN IN</div>

  <div class="footer-band">
    <span class="create-account">Create Account</span>
  </div>
</body>
</html>
```